New Business Card Design For Re-Branded Company (New Logo)

We recently switched our DBA and had a new logo designed. We now need new business cards made around our new logo. We would like to stick with the color scheme in our logo: White, Orange, and Blue. We want to see original bold designs that reflect our position in the solar energy sector but we prefer simple over complicated.

We are curious about vertical designs so if you can translate your design onto a vertical layout we would be open to look at it. We especially like a few designs we have seen on here that are vertical with a black or very dark gray background. They have our logo on one side and then the normal vertical business card on the other side.

I have included a screenshot of one of the samples we like, labeled sample.jpg and a file we were given as an example of our logo on a dark background.

At the same time we are satisfied to stay with what we have always had in a horizontal format. If it's not a lot of extra work for you, designs that are submitted in both horizontal and vertical formats will be greatly appreciated.

Please submit your original, bold, clean designs for consideration. Contact us with any questions or comments that may arise.

Thank you and Good Luck,

KP

```html
<!DOCTYPE html>
<html lang="en">
<head>
<meta charset="utf-8">
<title>Kestrel Power – Business Card</title>
<link rel="stylesheet" href="https://fonts.googleapis.com/css2?family=Open+Sans:wght@400;700;800&display=swap">
<style>
  :root {
    --page-bg: #e9e6e1;
    --card-bg: #2a2a2b;
    --card-edge: #1c1c1d;
    --orange: #f39a1e;
    --blue: #1e9ad6;
    --white: #ffffff;
    --text-soft: #e8e8e8;
    --ghost: #363637;
  }
  * { box-sizing: border-box; margin: 0; padding: 0; }
  html, body { width: 1200px; height: 780px; overflow: hidden; }
  body {
    background: var(--page-bg);
    font-family: "Open Sans", Verdana, sans-serif;
    display: flex;
    align-items: center;
    justify-content: center;
    gap: 90px;
  }
  .card {
    position: relative;
    width: 360px;
    height: 620px;
    background: var(--card-bg);
    border-radius: 4px;
    box-shadow: 0 3px 0 var(--card-edge), 0 6px 0 #222, 0 14px 30px rgba(0,0,0,.25);
    overflow: hidden;
  }
  /* front */
  .card-front .brand-dot {
    position: absolute;
    top: 42px;
    right: 40px;
    width: 150px;
    height: 150px;
    border-radius: 50%;
    border: 14px solid var(--blue);
  }
  .card-front .brand-name {
    position: absolute;
    top: 250px;
    left: 36px;
    font-size: 31px;
    font-weight: 700;
    color: var(--orange);
    letter-spacing: .5px;
  }
  .contact-block {
    position: absolute;
    left: 36px;
    top: 330px;
    color: var(--text-soft);
  }
  .person-name {
    font-size: 22px;
    font-weight: 800;
    color: var(--orange);
    letter-spacing: .5px;
  }
  .person-role { font-size: 17px; margin-bottom: 22px; }
  .address { font-size: 17px; line-height: 1.3; margin-bottom: 12px; }
  .contact-line {
    display: flex;
    align-items: center;
    gap: 10px;
    font-size: 17px;
    line-height: 1.5;
  }
  .contact-icon {
    width: 22px;
    height: 18px;
    background: var(--orange);
    border-radius: 2px;
    display: flex;
    align-items: center;
    justify-content: center;
  }
  .contact-icon svg { width: 14px; height: 12px; }
  /* back */
  .card-back .ghost-ring {
    position: absolute;
    left: 20px;
    top: 140px;
    width: 320px;
    height: 320px;
    border-radius: 50%;
    border: 22px solid var(--ghost);
  }
  .card-back .brand-name {
    position: absolute;
    left: 50%;
    top: 50%;
    transform: translate(-50%, -50%) rotate(90deg);
    white-space: nowrap;
    font-size: 50px;
    font-weight: 700;
    color: var(--orange);
    letter-spacing: 1px;
  }
</style>
</head>
<body>
  <article class="card card-front">
    <div class="brand-dot" aria-hidden="true"></div>
    <div class="brand-name">KESTREL POWER</div>
    <div class="contact-block">
      <div class="person-name">EMPLOYEE NAME</div>
      <div class="person-role">Owner</div>
      <div class="address">1111 Sample Lane<br>Fairview TX 00000 USA</div>
      <div class="contact-line">
        <span class="contact-icon"><svg viewBox="0 0 14 12"><path d="M3 1h2l1 3-1.5 1a6 6 0 0 0 3 3L9 6.5l3 1v2c0 .8-.7 1.5-1.5 1.5A9.5 9.5 0 0 1 1.5 2.5C1.5 1.7 2.2 1 3 1z" fill="#2a2a2b"/></svg></span>
        123-456-7890
      </div>
      <div class="contact-line">
        <span class="contact-icon"><svg viewBox="0 0 14 12"><rect x="3" y="1" width="8" height="4" fill="#2a2a2b"/><rect x="1" y="5" width="12" height="6" rx="1" fill="#2a2a2b"/></svg></span>
        123-456-7890
      </div>
      <div class="contact-line">
        <span class="contact-icon"><svg viewBox="0 0 14 12"><rect x="1" y="2" width="12" height="8" fill="none" stroke="#2a2a2b" stroke-width="1.4"/><path d="M1 2l6 5 6-5" fill="none" stroke="#2a2a2b" stroke-width="1.4"/></svg></span>
        hello@kestrelpower.com
      </div>
    </div>
  </article>

  <article class="card card-back">
    <div class="ghost-ring" aria-hidden="true"></div>
    <div class="brand-name">KESTREL POWER</div>
  </article>
</body>
</html>
```